Business card for a new innovative and professional lawn care business

We need a business card design for a new lawn care business in Halifax NS Canada. We offer lawn services in Halifax & Bedford. Our services offered include lawn care, garden services, and property maintenance. We take pride in our work and are experienced at what we do. I would like to see a design that is double sided. On the backside I would like the something simple (maybe my logo preferably on blackround (linked below) with website link, Facebook page or something). The front I want to include contact info:
Marcus Dell
phone 902-415-3968
email - brookvaleyards.ca
facebook - Facebook.com/brookvaleyards
Instagram maybe ? - instagram.com/brookvaleyard
Serving Halifax and Bedford for 5 years?
I don't want it to have too much information as I will be passing them out in aim to visit website, or call !
We do want it to include lawn care, garden services and property maintenance.
Basic, catchy, and modern looking !
Logo attached below !

Target Market(s)

Passing business cards to everyone I meet or interact with.

Industry/Entity Type

Lawn Care

Contact Information for Business Card

Double sided with some basic information, with catchy colours and easy to look at.

Font styles to use
Sans Serif

Requirements
Must have
• Must be double sided and have :
• Name, Phone, Email, FB, Website, and 3 main services offered - lawn care, property maintenance, garden services
Nice to have
• Would be nice to have instagram link if it goes well on there
Should not have
• Don't want too much writing or images that are distracting

```html
<!DOCTYPE html>
<html lang="en">
<head>
<meta charset="utf-8">
<title>Brookvale Yards – Business Card</title>
<link href="https://fonts.googleapis.com/css2?family=Lato:wght@400;700;900&display=swap" rel="stylesheet">
<style>
  :root {
    --page: #e4e4e4;
    --charcoal: #2e2e2e;
    --charcoal-edge: #3a3a3a;
    --lime: #7dc242;
    --forest: #1f7a3a;
    --paper: #ffffff;
    --ink: #1c1c1c;
    --dot: #f4f4f4;
  }
  * { box-sizing: border-box; margin: 0; padding: 0; }
  html, body {
    width: 1200px; height: 873px; overflow: hidden;
    background: var(--page);
    font-family: "Lato", Arial, sans-serif;
  }
  .stage {
    position: relative; width: 1200px; height: 873px;
    display: flex; align-items: center; justify-content: center; gap: 60px;
  }
  .card {
    position: relative; width: 520px; height: 300px;
    border-radius: 16px; overflow: hidden;
    box-shadow: 0 10px 30px rgba(0,0,0,.18);
  }

  /* Back side */
  .card--back { background: var(--charcoal); border: 1px solid var(--charcoal-edge); }
  .card--back .wordmark {
    position: absolute; top: 96px; left: 0; right: 0;
    display: flex; align-items: center; justify-content: center; gap: 14px;
  }
  .wordmark__dot { width: 22px; height: 22px; border-radius: 50%; background: var(--lime); }
  .wordmark__name {
    font-weight: 900; font-size: 40px; letter-spacing: 1px;
    color: var(--lime); text-transform: uppercase;
  }
  .services-band {
    position: absolute; left: 0; right: 0; bottom: 0; height: 34px;
    background: var(--lime);
    display: flex; align-items: center; justify-content: center; gap: 34px;
  }
  .service {
    display: flex; align-items: center; gap: 7px;
    font-size: 14px; font-weight: 700; color: var(--charcoal);
  }
  .service::before {
    content: ""; width: 7px; height: 7px; border-radius: 50%; background: var(--dot);
  }

  /* Front side */
  .card--front { background: var(--paper); }
  .owner-name {
    position: absolute; top: 34px; left: 0; right: 0; text-align: center;
    font-weight: 900; font-size: 20px; color: var(--lime); text-transform: uppercase;
  }
  .card--front .wordmark {
    position: absolute; top: 88px; left: 0; right: 0;
    display: flex; align-items: center; justify-content: center; gap: 12px;
  }
  .card--front .wordmark__name { color: var(--forest); font-size: 34px; }
  .card--front .wordmark__dot { background: var(--forest); width: 18px; height: 18px; }
  .contacts {
    position: absolute; left: 34px; right: 30px; bottom: 30px;
    display: flex; justify-content: space-between; align-items: flex-end;
  }
  .contact-list { list-style: none; display: flex; flex-direction: column; gap: 12px; }
  .contact {
    display: flex; align-items: center; gap: 10px;
    font-size: 16px; font-weight: 700; color: var(--ink);
  }
  .contact__icon {
    width: 24px; height: 24px; border-radius: 50%; background: var(--lime);
    display: flex; align-items: center; justify-content: center; flex: none;
  }
  .contact__icon svg { width: 14px; height: 14px; }
</style>
</head>
<body>
<main class="stage">

  <section class="card card--back" aria-label="Card back">
    <div class="wordmark">
      <span class="wordmark__dot"></span>
      <span class="wordmark__name">Brookvale Yards</span>
    </div>
    <div class="services-band">
      <span class="service">Lawn Care</span>
      <span class="service">Property Maintenance</span>
      <span class="service">Garden Services</span>
    </div>
  </section>

  <section class="card card--front" aria-label="Card front">
    <h1 class="owner-name">Marcus Dell</h1>
    <div class="wordmark">
      <span class="wordmark__dot"></span>
      <span class="wordmark__name">Brookvale Yards</span>
    </div>
    <div class="contacts">
      <ul class="contact-list">
        <li class="contact">
          <span class="contact__icon">
            <svg viewBox="0 0 24 24"><path fill="#fff" d="M6.6 10.8a15.2 15.2 0 0 0 6.6 6.6l2.2-2.2c.3-.3.7-.4 1-.2 1.1.4 2.3.6 3.6.6.6 0 1 .4 1 1V20c0 .6-.4 1-1 1A17 17 0 0 1 3 4c0-.6.4-1 1-1h3.5c.6 0 1 .4 1 1 0 1.2.2 2.4.6 3.6.1.3 0 .7-.2 1z"/></svg>
          </span>
          902-415-3968
        </li>
        <li class="contact">
          <span class="contact__icon">
            <svg viewBox="0 0 24 24"><rect x="3" y="6" width="18" height="12" rx="1.5" fill="none" stroke="#fff" stroke-width="2"/><path d="M3.5 7l8.5 6 8.5-6" fill="none" stroke="#fff" stroke-width="2"/></svg>
          </span>
          hello@brookvaleyards.ca
        </li>
      </ul>
      <ul class="contact-list">
        <li class="contact">
          <span class="contact__icon"></span>
          /brookvaleyards
        </li>
        <li class="contact">
          <span class="contact__icon">
            <svg viewBox="0 0 24 24"><circle cx="12" cy="12" r="8.5" fill="none" stroke="#fff" stroke-width="2"/><path d="M3.5 12h17M12 3.5c3 3 3 14 0 17M12 3.5c-3 3-3 14 0 17" fill="none" stroke="#fff" stroke-width="1.6"/></svg>
          </span>
          www.brookvaleyards.ca
        </li>
      </ul>
    </div>
  </section>

</main>
</body>
</html>
```